Postcard Design

Looking for 4.25 x6 postcard design for mass mailing
Design should be eye catching, energetic and draw the viewer in

Data for postcard to include:
Logo and slogan
Pediatric Occupational, Physical and Speech Therapy Services; Assistive Technology Evaluation and Training

Speech-Language Therapy
oral motor skills
speech delays
language skills
Articulation
Voice
fluency
cognitive skills
feeding disorders
Play skills

OCCUPATIONAL THERAPY
Our occupational therapists use play in therapy to help your child develop the skills he/she needs to perform their job of living and playing, including but not limited to:
- Increasing independence in self-care skills such as feeding, dressing and grooming
- Improving developmental skills such as rolling, sitting, standing
- Improving their sensory processing, balance, coordination and motor planning
- Difficulty tolerating clothing
- Poor balance - doesn't ride a bike/climb on slides, falls frequently, cries when moved unexpectedly
- Intolerance to textures/odors/loud sounds/movement
- Delayed handwriting and fine motor skills and/or
avoids fine motor activities such as using crayons, fasteners on clothing, pencils
- Limited diet-refuses to try new foods, gags when trying new tastes, textures
- Appears extremely anxious, states frequent fears of harmless things

CONTACT US TODAY for a FREE 15 minute consultation/Screen
(301) 555-4182
info@brightwillowkids.example
www.brightwillowkids.example

Physical therapy
Delayed crawling / walking
Persistent toe walking habits
Poor unsupported sitting/standing balance
Trouble learning how to jump, skip, ride a bike
Decreased ability to throw and catch a ball
Delayed motor milestones
Need for wheelchair mobility training
Balance coordination and motor planning difficulty
Strength , muscle tone and/ R range of motion impairment
Sports injuries
Postural control and positioning difficulty

```html
<!DOCTYPE html>
<html lang="en">
<head>
<meta charset="utf-8">
<title>Bright Willow Kids – Postcard</title>
<link rel="stylesheet" href="https://fonts.googleapis.com/css2?family=Roboto+Condensed:wght@500;700&family=Open+Sans:ital,wght@0,400;0,600;0,700;0,800;1,400&display=swap">
<style>
:root{
  --bg:#7a7a7a;
  --teal:#179c98;
  --teal-dark:#12807d;
  --blue:#1769c7;
  --blue-light:#2b8fd6;
  --yellow:#f6c545;
  --orange:#e99148;
  --white:#ffffff;
  --ink:#1d3c52;
  --paper:#f1f5f7;
  --stamp:#dcdcdc;
}
*{box-sizing:border-box;margin:0;padding:0}
html,body{width:686px;height:1200px;overflow:hidden}
body{background:var(--bg);font-family:"Open Sans",Arial,sans-serif;position:relative}
.card{position:absolute;left:43px;width:600px;height:450px;overflow:hidden;box-shadow:0 4px 14px rgba(0,0,0,.35);background:var(--white)}
.card--front{top:110px}
.card--back{top:640px}

/* front */
.photo-column{position:absolute;left:0;top:0;width:172px;height:410px;display:flex;flex-direction:column}
.photo{flex:1;border-bottom:3px solid var(--white)}
.photo--reading{background:linear-gradient(135deg,#f4d6d6,#e8e2dc 60%,#d8c7b6)}
.photo--playing{background:linear-gradient(135deg,#3a3f45,#c8403c 55%,#e9d6a8)}
.photo--writing{background:linear-gradient(135deg,#d9d2c6,#6b4a35 55%,#b74436);border-bottom:0}
.front-main{position:absolute;left:172px;top:0;width:428px;height:410px}
.front-header{height:150px;background:linear-gradient(90deg,var(--paper),var(--white));text-align:center;padding-top:14px}
.brand{display:inline-flex;align-items:center;gap:7px;font-family:"Open Sans",sans-serif;font-weight:700;color:var(--teal-dark);font-size:17px}
.brand__dot{width:14px;height:14px;border-radius:50%;background:var(--teal)}
.slogan{font-size:7.5px;font-style:italic;color:var(--ink);margin-top:2px}
.services-title{font-family:"Roboto Condensed",sans-serif;font-weight:700;color:var(--teal-dark);font-size:17px;line-height:1.35;margin-top:12px;text-transform:uppercase}
.section{position:relative}
.section--speech{height:88px;background:linear-gradient(90deg,var(--teal),var(--blue-light));padding:18px 14px 0}
.section--physical{height:172px;background:linear-gradient(180deg,var(--yellow),var(--orange));padding:22px 14px 0}
.pill{position:absolute;left:50%;transform:translateX(-50%);top:-9px;font-family:"Open Sans",sans-serif;font-weight:800;font-size:10px;letter-spacing:.3px;padding:3px 16px;border-radius:12px;white-space:nowrap;text-transform:uppercase}
.pill--yellow{background:var(--yellow);color:var(--white)}
.pill--teal{background:var(--teal);color:var(--white)}
.tick-list{list-style:none;display:grid;column-gap:10px;row-gap:5px}
.tick-list li{position:relative;padding-left:14px;font-size:9.5px;line-height:1.2;color:var(--white);font-weight:600}
.tick-list li::before{content:"";position:absolute;left:0;top:1px;width:9px;height:9px;border-radius:50%;border:1px solid currentColor}
.tick-list li::after{content:"";position:absolute;left:3px;top:3px;width:3px;height:4px;border:solid currentColor;border-width:0 1.2px 1.2px 0;transform:rotate(45deg)}
.tick-list--three{grid-template-columns:repeat(3,1fr);row-gap:6px}
.tick-list--physical{grid-template-columns:1fr 1fr;width:300px;row-gap:3px;grid-auto-flow:column;grid-template-rows:repeat(6,auto)}
.tick-list--physical li{font-size:9px}
.photo--therapist{position:absolute;right:8px;bottom:4px;width:96px;height:96px;background:linear-gradient(160deg,#f5e8d8,#e1a24c 60%,#4a6c8c);border-radius:4px;opacity:.9}
.contact-bar{position:absolute;left:0;bottom:0;width:600px;height:40px;background:linear-gradient(90deg,var(--blue),var(--blue-light));display:flex;align-items:center;justify-content:space-around;color:var(--white);font-size:11px}
.contact-bar span{display:inline-flex;align-items:center;gap:6px}
.contact-bar svg{width:12px;height:12px}

/* back */
.back-panel{position:absolute;left:0;top:0;width:318px;height:450px;background:linear-gradient(180deg,var(--teal) 0%,var(--blue-light) 55%,var(--blue) 75%)}
.back-panel .pill{top:12px}
.ot-intro{position:absolute;left:18px;top:42px;width:290px;font-size:9.5px;font-weight:700;line-height:1.3;color:var(--white)}
.ot-list{position:absolute;left:18px;top:100px;width:292px;list-style:none}
.ot-list li{position:relative;padding-left:14px;font-size:8px;font-style:italic;line-height:1.25;color:var(--white);margin-bottom:6px}
.ot-list li::before{content:"";position:absolute;left:0;top:1px;width:8px;height:8px;border-radius:50%;border:1px solid var(--yellow)}
.ot-list li::after{content:"";position:absolute;left:3px;top:2.5px;width:2.5px;height:4px;border:solid var(--yellow);border-width:0 1.2px 1.2px 0;transform:rotate(45deg)}
.cta-cloud{position:absolute;left:0;bottom:0;width:318px;height:120px}
.photo--group{position:absolute;left:220px;top:300px;width:88px;height:50px;background:linear-gradient(135deg,#f0e2c8,#3d5d8a 50%,#c64a3a);border:2px solid var(--white)}
.cta{position:absolute;left:0;bottom:10px;width:318px;text-align:center;color:var(--white);font-family:"Roboto Condensed",sans-serif;font-weight:700;text-transform:uppercase}
.cta__lead{font-size:13px}
.cta__offer{font-size:26px;line-height:1.05}
.cta__tail{font-size:15px}
.cta__phone{font-size:17px;color:var(--blue);display:inline-flex;align-items:center;gap:5px;margin-top:4px}
.cta__phone svg{width:14px;height:14px}
.address-side .brand{position:absolute;left:334px;top:40px;font-size:11px;gap:5px}
.address-side .brand__dot{width:9px;height:9px}
.stamp-box{position:absolute;right:22px;top:25px;width:44px;height:48px;background:var(--stamp)}
.url-pill{position:absolute;right:24px;bottom:18px;background:var(--teal);color:var(--white);font-size:10px;font-weight:600;padding:4px 16px;border-radius:12px}
</style>
</head>
<body>

<section class="card card--front">
  <div class="photo-column">
    <div class="photo photo--reading" role="img" aria-label="Photo of a therapist reading with a young girl"></div>
    <div class="photo photo--playing" role="img" aria-label="Photo of a boy playing with a toy"></div>
    <div class="photo photo--writing" role="img" aria-label="Photo of a child practising handwriting"></div>
  </div>
  <div class="front-main">
    <header class="front-header">
      <div class="brand"><span class="brand__dot"></span>Bright Willow Kids</div>
      <p class="slogan">Improving skills and function for daily living</p>
      <h1 class="services-title">Pediatric Occupational &nbsp;|&nbsp; Physical and Speech<br>Therapy Services &nbsp;|&nbsp; Assistive<br>Technology Evaluation and Training</h1>
    </header>
    <div class="section section--speech">
      <h2 class="pill pill--yellow">Speech-Language Therapy</h2>
      <ul class="tick-list tick-list--three">
        <li>Oral motor skills</li><li>Articulation</li><li>Cognitive skills</li>
        <li>Speech delays</li><li>Voice</li><li>Feeding disorders</li>
        <li>Language skills</li><li>Fluency</li><li>Play skills</li>
      </ul>
    </div>
    <div class="section section--physical">
      <h2 class="pill pill--teal">Physical Therapy</h2>
      <ul class="tick-list tick-list--physical">
        <li>Delayed crawling / walking</li>
        <li>Persistent toe walking habits</li>
        <li>Poor unsupported sitting/standing balance</li>
        <li>Trouble learning how to jump, skip, ride a bike</li>
        <li>Decreased ability to throw and catch a ball</li>
        <li>Delayed motor milestones</li>
        <li>Need for wheelchair mobility training</li>
        <li>Balance coordination and motor planning difficulty</li>
        <li>Strength , muscle tone and / R range of motion impairment</li>
        <li>Sports injuries</li>
        <li>Postural control and positioning difficulty</li>
      </ul>
      <div class="photo--therapist" role="img" aria-label="Photo of a therapist helping a child stretch"></div>
    </div>
  </div>
  <footer class="contact-bar">
    <span><svg viewBox="0 0 24 24"><path fill="var(--yellow)" d="M6.6 10.8a15 15 0 0 0 6.6 6.6l2.2-2.2c.3-.3.7-.4 1-.2 1.1.4 2.3.6 3.6.6.6 0 1 .4 1 1V20c0 .6-.4 1-1 1A17 17 0 0 1 3 4c0-.6.4-1 1-1h3.5c.6 0 1 .4 1 1 0 1.3.2 2.5.6 3.6.1.3 0 .7-.2 1z"/></svg>(301) 555-4182</span>
    <span><svg viewBox="0 0 24 24"><rect x="2" y="5" width="20" height="14" rx="2" fill="var(--yellow)"/><path d="M3 6l9 7 9-7" fill="none" stroke="var(--blue)" stroke-width="1.6"/></svg>info@brightwillowkids.example</span>
    <span><svg viewBox="0 0 24 24"><circle cx="12" cy="12" r="9.5" fill="none" stroke="var(--yellow)" stroke-width="2"/><path d="M2.5 12h19M12 2.5c3 3 3 16 0 19M12 2.5c-3 3-3 16 0 19" fill="none" stroke="var(--yellow)" stroke-width="1.5"/></svg>www.brightwillowkids.example</span>
  </footer>
</section>

<section class="card card--back">
  <div class="back-panel">
    <h2 class="pill pill--yellow">Occupational Therapy</h2>
    <p class="ot-intro">Our occupational therapists use play in therapy to help your child develop the skills he/she needs to perform their job of living and playing, including but not limited to:</p>
    <ul class="ot-list">
      <li>Increasing independence in self-care skills such as feeding, dressing and grooming</li>
      <li>Improving developmental skills such as rolling, sitting, standing</li>
      <li>Improving their sensory processing, balance, coordination and motor planning</li>
      <li>Difficulty tolerating clothing</li>
      <li>Poor balance - doesn't ride a bike/climb on slides, falls frequently, cries when moved unexpectedly</li>
      <li>Intolerance to textures/odors/loud sounds/movement</li>
      <li>Delayed handwriting and fine motor skills and/or avoids fine motor activities such as using crayons, fasteners on clothing, pencils</li>
      <li>Limited diet-refuses to try new foods, gags when trying new tastes, textures</li>
      <li>Appears extremely anxious, states frequent fears of harmless things</li>
    </ul>
    <svg class="cta-cloud" viewBox="0 0 318 120" preserveAspectRatio="none" aria-hidden="true">
      <defs><linearGradient id="ctaFill" x1="0" y1="0" x2="0" y2="1"><stop offset="0" stop-color="#f0a24f"/><stop offset="1" stop-color="#f6c545"/></linearGradient></defs>
      <path fill="url(#ctaFill)" d="M0 30 Q12 10 30 22 Q45 2 66 18 Q82 6 98 20 Q118 4 138 22 Q160 10 178 26 Q200 12 214 30 L318 30 L318 120 L0 120 Z"/>
    </svg>
    <div class="photo--group" role="img" aria-label="Photo of a smiling group of children"></div>
    <div class="cta">
      <p class="cta__lead">Contact us today for a</p>
      <p class="cta__offer">Free 15 Minute</p>
      <p class="cta__tail">Consultation/Screen</p>
      <p class="cta__phone"><svg viewBox="0 0 24 24"><path fill="var(--blue)" d="M6.6 10.8a15 15 0 0 0 6.6 6.6l2.2-2.2c.3-.3.7-.4 1-.2 1.1.4 2.3.6 3.6.6.6 0 1 .4 1 1V20c0 .6-.4 1-1 1A17 17 0 0 1 3 4c0-.6.4-1 1-1h3.5c.6 0 1 .4 1 1 0 1.3.2 2.5.6 3.6.1.3 0 .7-.2 1z"/></svg>(301) 555-4182</p>
    </div>
  </div>
  <div class="address-side">
    <div class="brand"><span class="brand__dot"></span>Bright Willow Kids</div>
    <div class="stamp-box"></div>
    <p class="url-pill">www.brightwillowkids.example</p>
  </div>
</section>

</body>
</html>
```